Business card design needed

We are a wine business involved in winemaking, broking and packaging on behalf of clients globally with the majority being Asian. The design should be quite traditional and classic with some red used, font used should be easily read.

Target Market(s)

Trade customers other business owners

Industry/Entity Type

Business

Contact Information for Business Card

Rosalind Whitcombe
Meridale Wine Collective
PO Box 738, Fenwick Vale
South Australia 5287
Phone: +61 (0)487 263 918
Email: mvcellar@brindlenet.com.au

Logo styles of interest
Lettermark Logo

```html
<!DOCTYPE html>
<html lang="en">
<head>
<meta charset="utf-8">
<title>Meridale Wine Collective – Business Card</title>
<link href="https://fonts.googleapis.com/css2?family=Cinzel:wght@400;700&display=swap" rel="stylesheet">
<style>
  :root {
    --backdrop: #e8e3dc;
    --card-dark: #000000;
    --card-light: #ffffff;
    --ink-dark: #111111;
    --ink-light: #ffffff;
    --accent-red: #ec2227;
  }
  html, body {
    margin: 0;
    padding: 0;
    width: 1200px;
    height: 800px;
    overflow: hidden;
    background: var(--backdrop);
  }
  .canvas {
    position: relative;
    width: 1200px;
    height: 800px;
  }
  .card {
    position: absolute;
    width: 657px;
    height: 405px;
    box-shadow: 0 3px 10px rgba(0, 0, 0, 0.25);
  }
  .card-front {
    left: 53px;
    top: 57px;
    background: var(--card-dark);
    display: flex;
    flex-direction: column;
    align-items: center;
    justify-content: center;
  }
  .brand-dot {
    width: 34px;
    height: 34px;
    border-radius: 50%;
    background: var(--accent-red);
    margin-bottom: 26px;
  }
  .brand-name {
    font-family: "Cinzel", serif;
    font-weight: 400;
    font-size: 21px;
    letter-spacing: 0.08em;
    color: var(--ink-light);
    margin: 0;
  }
  .card-back {
    left: 490px;
    top: 360px;
    background: var(--card-light);
  }
  .holder-name {
    position: absolute;
    top: 148px;
    left: 0;
    right: 0;
    text-align: center;
    font-family: "Cinzel", serif;
    font-weight: 700;
    font-size: 27px;
    letter-spacing: 0.03em;
    color: var(--ink-dark);
    margin: 0;
  }
  .contact-details {
    position: absolute;
    top: 268px;
    left: 0;
    right: 0;
    text-align: center;
    font-family: "Cinzel", serif;
    font-weight: 400;
    font-size: 17.5px;
    line-height: 23px;
    color: var(--ink-dark);
    text-transform: uppercase;
    font-style: normal;
  }
  .accent-band {
    position: absolute;
    left: 0;
    right: 0;
    top: 371px;
    height: 26px;
    background: var(--accent-red);
  }
</style>
</head>
<body>
  <main class="canvas">
    <section class="card card-front">
      <div class="brand-dot"></div>
      <p class="brand-name">Meridale Wine Collective</p>
    </section>

    <section class="card card-back">
      <h1 class="holder-name">Rosalind Whitcombe</h1>
      <address class="contact-details">
        PO Box 738, Fenwick Vale South Australia 5287<br>
        +61 (0)487 263 918<br>
        mvcellar@brindlenet.com.au
      </address>
      <div class="accent-band"></div>
    </section>
  </main>
</body>
</html>
```